Layout for new page on existing website

We have an existing website (www.brightloomworks.org) and need a new page designing to promote a new product.
The new page needs to be consistent with the existing website look and feel (www.brightloomworks.org) but current persistent elements on the standard page design can be moved/removed from the page to accommodate a new layout necessary for getting all the content laid out in a logical user friendly way.
The content required for the page is attached along with a wireframe mock up that may help understand the expectation, however the wireframe was just created to help me work out what was needed on the page and the layout can be different. A key element is the quality of the design of each of the artifacts (e.g. the panel the embedded video needs to go in, icons etc) and a clear display of the information.
Updates
The website that the new page needs to fit into is www.brightloomworks.org, i will also added the company logo to the brief.
Our Corporate Colours
- Green: #A2FF00
- Cream: #FFFF99
- Yellow: #FFE900
- Grey: #534741
Industry/Entity Type
Product
Look and feel
Each slider illustrates characteristics of the customer's brand and the style your logo design should communicate.

```html
<!DOCTYPE html>
<html lang="en">
<head>
<meta charset="utf-8">
<title>Brightloom Works – Course Management and Booking</title>
<link href="https://fonts.googleapis.com/css2?family=Ubuntu:wght@400;500;700&family=Russo+One&display=swap" rel="stylesheet">
<style>
:root{
  --bg:#4e403a;
  --bg-edge:#43362f;
  --panel:#5c4c45;
  --panel-inner:#62524b;
  --line:#a3958d;
  --green:#a2ff00;
  --cream:#ffff99;
  --yellow:#ffe900;
  --title:#f2e84a;
  --text:#ece4dc;
  --orange:#e07000;
}
*{margin:0;padding:0;box-sizing:border-box}
html,body{width:689px;height:1200px;overflow:hidden}
body{background:linear-gradient(90deg,var(--bg-edge) 0 22px,var(--bg) 22px 667px,var(--bg-edge) 667px);font-family:"Ubuntu",sans-serif;color:var(--text);position:relative}
.abs{position:absolute}
.home{left:56px;top:34px;width:40px;text-align:center;font-size:8px;font-weight:700;color:#fff}
.home svg{display:block;margin:0 auto 8px}
.brand{left:180px;top:60px;width:320px;text-align:center;font-size:20px;font-weight:700;letter-spacing:5px;color:#fff;display:flex;align-items:center;justify-content:center;gap:10px}
.brand-dot{width:14px;height:14px;border-radius:50%;background:var(--green)}
.headline{left:0;width:689px;text-align:center;font-family:"Russo One",sans-serif;color:var(--title);font-size:17px}
.hero{left:33px;top:129px;width:623px;height:195px;border:1px solid var(--line);border-radius:7px;background:linear-gradient(90deg,#2d2a2a 0%,#504a48 40%,#8a8d92 70%,#b9c2c9 100%)}
.box{border:1px solid var(--line);background:var(--panel)}
.video{left:33px;top:357px;width:311px;height:177px;background:#000;border:1px solid var(--orange)}
.play-big{left:126px;top:54px;width:59px;height:51px;background:var(--orange);border:1px solid #f5a040}
.controls{left:4px;bottom:4px;right:4px;height:20px}
.testi{left:354px;top:357px;width:302px;height:177px;padding:6px 7px}
h2{font-weight:400;color:var(--cream);font-size:13px}
.testi p{font-size:7.6px;line-height:14px;margin:6px 4px 0}
.testi .who{font-size:9.5px;color:var(--cream);line-height:16px;margin-top:10px}
.features{left:33px;top:540px;width:623px;height:279px}
.col{top:6px;height:266px;background:var(--panel-inner)}
.col.left{left:5px;width:292px;padding:8px 6px}
.col.right{left:307px;width:310px;padding:22px 8px}
.feat h3{font-weight:400;color:var(--cream);font-size:10.5px;display:flex;align-items:center;gap:6px;margin-bottom:7px}
.feat p{font-size:7.6px;line-height:12.5px}
.benefits{left:33px;top:826px;width:623px;height:133px;padding:5px 7px}
.benefits p{font-size:7.6px;line-height:11.6px;margin-top:3px}
.bubble{left:116px;top:981px;width:144px;height:144px;border-radius:50%;background:#fff;border:5px solid var(--cream);box-shadow:0 0 0 2px #f0f04a;text-align:center;font-size:8.8px;line-height:17.5px;color:#3b302b;padding-top:17px}
.form{left:272px;top:988px;width:302px;height:136px;padding:14px 0 0 34px}
.row{display:flex;align-items:center;height:19.5px;font-size:7.6px}
.row label{width:112px}
.row span{width:121px;height:13px;background:#fff}
.send{left:119px;top:107px;width:60px;height:17px;background:linear-gradient(#b8ff40,#7cd000);border:1px solid #cfff80;color:#2a2a00;font-size:10px;font-weight:700;text-align:center;line-height:15px}
.footer{left:0;top:1157px;width:689px;text-align:center;font-size:7.6px}
</style>
</head>
<body>
<div class="abs home">
  <svg width="30" height="28" viewBox="0 0 30 28"><circle cx="15" cy="14" r="13" fill="#ffe900" opacity=".25"/><path d="M5 14 15 5l10 9M8 12v11h14V12" fill="none" stroke="#ffe900" stroke-width="2"/><rect x="13" y="16" width="4" height="7" fill="#ffe900"/></svg>
  Home
</div>
<div class="abs brand"><span>BRIGHTLOOM WORKS</span><span class="brand-dot"></span></div>
<div class="abs headline" style="top:102px">Course Management and Booking Simplified</div>
<div class="abs hero" role="img" aria-label="Photo of business people meeting around a boardroom table"></div>
<div class="abs headline" style="top:330px">Built with only Your business in mind</div>

<div class="abs video">
  <div class="abs play-big"><svg width="59" height="51" viewBox="0 0 59 51"><path d="M24 15v21l16-10.5z" fill="#fff"/></svg></div>
  <svg class="abs controls" viewBox="0 0 303 20" width="303" height="20"><rect x="0" y="0" width="32" height="20" fill="#e07000"/><path d="M12 5v10l9-5z" fill="#fff"/><rect x="37" y="2" width="20" height="6" fill="#fff"/><rect x="40" y="10" width="233" height="5" fill="#333" stroke="#777" stroke-width=".5"/><rect x="40" y="10" width="30" height="5" fill="#888"/><g fill="#e07000"><rect x="280" y="8" width="2" height="7"/><rect x="283" y="8" width="2" height="7"/><rect x="286" y="8" width="2" height="7"/><rect x="289" y="8" width="2" height="7"/></g><rect x="294" y="9" width="6" height="6" fill="none" stroke="#ccc"/></svg>
</div>

<div class="abs box testi">
  <h2>Testimonials</h2>
  <p>"A convenient tool that was simple to integrate into our website. It has allowed both the business and our customers an easy way to book courses. In life sometimes simple is good and this is a great example!"</p>
  <p class="who">Clara Wendell, Director @ TrainNest<br>www.trainnest.org</p>
</div>

<div class="abs box features">
  <div class="abs col left">
    <h2 style="margin-bottom:4px">key features</h2>
    <div class="feat"><h3><svg width="11" height="11"><circle cx="5.5" cy="5.5" r="5" fill="#3c9a3c"/><path d="M5.5 2.5v3h2.5" stroke="#fff" fill="none"/></svg>Available and easy to use 24/7</h3>
    <p>By allowing booking and payment at any time of<br>the day, your attendees will be more likely to commit to your event and with no account setup or password required and no paper forms to fill in and post, booking onto and paying for your courses is easy.</p></div>
    <div class="feat" style="margin-top:28px"><h3><svg width="16" height="16"><path d="M6 1h4v5h5v4h-5v5H6v-5H1V6h5z" fill="#3c9a3c"/></svg>Online Course promotion</h3>
    <p>List your upcoming courses in a clear and simple way so people can easily find and select the course that suits them.</p></div>
    <div class="feat" style="margin-top:5px"><h3><svg width="14" height="12"><rect x="0" y="2" width="14" height="10" fill="#3c9a3c"/><rect x="2" y="4" width="9" height="3" fill="#fff"/></svg>Online &amp; Offline Payments</h3>
    <p>Take payments online, whilst having the flexibility of managing and adding offline payments.</p></div>
  </div>
  <div class="abs col right">
    <div class="feat"><h3><svg width="14" height="11"><rect x="0" y="0" width="14" height="11" fill="#3c9a3c"/><path d="M0 0l7 6 7-6" stroke="#fff" fill="none"/></svg>Built in email system</h3>
    <p>Enable quick and easy communication with upcoming course candidates and promotion of additional courses to past candidates.</p></div>
    <div class="feat" style="margin-top:12px"><h3><svg width="12" height="14"><path d="M10 1 3 9 1 13l4-2 7-8z" fill="#3c9a3c"/></svg>Customisable look and feel</h3>
    <p>All elements of the booking systems design will fit in with your existing websites style.</p></div>
    <div class="feat" style="margin-top:12px"><h3><svg width="12" height="14"><circle cx="6" cy="4" r="3.5" fill="#3c9a3c"/><path d="M0 14c0-6 12-6 12 0z" fill="#3c9a3c"/></svg>Live course place availability</h3>
    <p>By defining minimum and maximum candidates permitted on a course its easy to prevent overbooking and also prevent courses running that don't have enough<br>candidates.</p></div>
    <div class="feat" style="margin-top:6px"><h3><svg width="14" height="16"><rect x="1" y="1" width="12" height="15" fill="#3c9a3c"/><rect x="3" y="3" width="6" height="5" fill="#fff"/></svg>Venue database management</h3>
    <p>Easily add, edit and remove venues from which you operate your courses from.</p></div>
  </div>
</div>

<div class="abs box benefits">
  <h2>key Benefits</h2>
  <p>Live Availability - Availability on course place availability to prevent overbooking Customers can search for Courses and Book Online with immediate confirmation Automated confirmation emails Be available for business 24/7 and take orders anytime! Customers can book when it's most convenient for them - be it early morning, late evening or weekend No fielding phone calls, no wading through paper registrations. Attendees book on your website, there and then No more trips to the bank, take immediate and secure payments online Automated confirmation emails so reducing the time need communicating with candidates Boost course bookings and reduce administrative time and costs Course Admin is Web based meaning you can access your course information from anywhere at any time. System is very intuitive and easy to use. Lighten your workload Upload and manage offline bookings through the admin dashboard Keep your attendees organized all the way up to the course date and beyond</p>
  <p style="margin-top:11px">Contact Us Now for a free no obligation discussion about your requirement and quote.</p>
</div>

<div class="abs bubble">Contact Us Now<br>For A Free<br>No Obligation Discussion<br>About Your Requirement<br>And Quote</div>

<div class="abs box form">
  <div class="row"><label>Name *</label><span></span></div>
  <div class="row"><label>Company Name *</label><span></span></div>
  <div class="row"><label>Email *</label><span></span></div>
  <div class="row"><label>Telephone *</label><span></span></div>
  <div class="abs send">SEND</div>
</div>

<div class="abs footer">|© 2010 Brightloom Works, All Rights Reserved | Disclaimer |</div>
</body>
</html>
```